Business Cards and Stationery for Mechanical Contractor
Stalwart Ductworks Contractors, Inc.
Business Cards and Stationery for Mechanical Contractor - Construction
Creative Brief
Professional
Howard Pelley
President
3148 Foundry Ave. Fort Wayne, IN 46139
hpelley@stalwartducts.example
www.StalwartDucts.example

```html
<!DOCTYPE html>
<html lang="en">
<head>
<meta charset="utf-8">
<title>Stalwart Ductworks Contractors, Inc. — Business Cards</title>
<link rel="stylesheet" href="https://fonts.googleapis.com/css2?family=Roboto+Condensed:wght@400;700&display=swap">
<style>
  :root {
    --bg: #8a8c8e;
    --green: #2f8f3e;
    --green-dark: #23722f;
    --green-light: #3aa34a;
    --black: #141414;
    --white: #ffffff;
    --ink: #1f1f1f;
  }
  * { margin: 0; padding: 0; box-sizing: border-box; }
  html, body { width: 1200px; height: 908px; overflow: hidden; }
  body {
    background: var(--bg);
    font-family: "Roboto Condensed", Arial, sans-serif;
    position: relative;
  }
  .card {
    position: absolute;
    top: 304px;
    width: 525px;
    height: 300px;
    border-radius: 18px;
    overflow: hidden;
    box-shadow: 0 10px 24px rgba(0,0,0,0.3);
  }
  .card-front {
    left: 50px;
    background: radial-gradient(ellipse at 75% 40%, var(--green-light) 0%, var(--green) 45%, var(--green-dark) 100%);
  }
  .card-back { left: 625px; background: var(--white); }
  .card-back svg.shapes { position: absolute; inset: 0; }

  .brand {
    position: absolute;
    display: flex;
    align-items: center;
    gap: 10px;
    font-weight: 700;
    line-height: 1.1;
  }
  .brand-mark { width: 16px; height: 16px; border-radius: 50%; flex: none; }
  .card-front .brand { left: 40px; top: 118px; color: var(--white); font-size: 21px; }
  .card-front .brand-mark { background: var(--white); }
  .card-back .brand { left: 36px; top: 110px; color: var(--green-dark); font-size: 19px; }
  .card-back .brand-mark { background: var(--green-dark); }

  .person {
    position: absolute;
    right: 24px;
    top: 47px;
    text-align: right;
    color: var(--white);
  }
  .person-name { font-size: 19px; font-weight: 700; }
  .person-title { font-size: 13px; }

  .contact {
    position: absolute;
    left: 36px;
    top: 200px;
    color: var(--white);
    font-size: 13px;
    line-height: 1.3;
    list-style: none;
  }
  .contact li { display: flex; align-items: center; gap: 6px; }
  .contact svg { width: 12px; height: 12px; flex: none; }
</style>
</head>
<body>

<section class="card card-front" aria-label="Business card front">
  <div class="brand">
    <span class="brand-mark"></span>
    <span class="brand-name">Stalwart Ductworks<br>Contractors, Inc.</span>
  </div>
</section>

<section class="card card-back" aria-label="Business card back">
  <svg class="shapes" viewBox="0 0 525 300" width="525" height="300" aria-hidden="true">
    <polygon points="0,188 300,188 362,112 525,112 525,300 0,300" fill="var(--green)"/>
    <polygon points="398,38 525,38 525,104 345,104" fill="var(--black)"/>
    <line x1="36" y1="162" x2="300" y2="162" stroke="var(--green-dark)" stroke-width="2"/>
  </svg>

  <div class="brand">
    <span class="brand-mark"></span>
    <span class="brand-name">Stalwart Ductworks<br>Contractors, Inc.</span>
  </div>

  <div class="person">
    <div class="person-name">Howard Pelley</div>
    <div class="person-title">President</div>
  </div>

  <ul class="contact">
    <li>3148 Foundry Ave.</li>
    <li>Fort Wayne, IN 46139</li>
    <li>
      <svg viewBox="0 0 12 12"><circle cx="6" cy="6" r="5.5" fill="none" stroke="currentColor"/><path d="M4 3.5l1 1.5-.6.6c.4.8 1 1.4 1.8 1.8l.6-.6 1.5 1-.6 1C5.5 8.6 3.4 6.5 3 4.1z" fill="currentColor"/></svg>
      260-555-0147
    </li>
    <li>
      <svg viewBox="0 0 12 12"><circle cx="6" cy="6" r="5.5" fill="none" stroke="currentColor"/><rect x="3.5" y="3" width="5" height="6" fill="none" stroke="currentColor"/></svg>
      260-555-0193
    </li>
    <li>
      <svg viewBox="0 0 12 12"><circle cx="6" cy="6" r="5.5" fill="none" stroke="currentColor"/><rect x="3" y="4" width="6" height="4" fill="none" stroke="currentColor"/><path d="M3 4l3 2.2L9 4" fill="none" stroke="currentColor"/></svg>
      hpelley@stalwartducts.example
    </li>
    <li>
      <svg viewBox="0 0 12 12"><circle cx="6" cy="6" r="5.5" fill="none" stroke="currentColor"/><ellipse cx="6" cy="6" rx="2" ry="4" fill="none" stroke="currentColor"/><line x1="2" y1="6" x2="10" y2="6" stroke="currentColor"/></svg>
      www.StalwartDucts.example
    </li>
  </ul>
</section>

</body>
</html>
```